we are a mobile auto windscreen replacement business we are looking for a smart, stylish designed card on a matte black base color with large metallic silver KVT (similar to the zenpod box)
over the whole face of the card but down the bottom have (your local automotive & machinery glass specialist) & over the back

Reason: I'm looking for a design like no other something that really wows people to grab a card & use my business

Target Market(s)

Adults in western countries that own an automotive fleet company or anybody that owns a car

Industry/Entity Type

Automotive

Contact Information for Business Card

front: KVTglassworks
Back: MORRIS 0482 65 71 93 Abn: 52840193657
morris@kvtglassworks.com.au & www.kvtglassworks.com.au

Logo styles of interest
Lettermark Logo
Requirements
Must have
• Metallic font on matte background
Nice to have
• 3D font that's glass or the word KVT smashed into glass on a black background I've added some pictures that maybe you could incorporate in the background or font it would be great to see a professionals ideas

```html
<!DOCTYPE html>
<html lang="en">
<head>
<meta charset="utf-8">
<title>KVTglassworks – Business Card</title>
<link rel="stylesheet" href="https://fonts.googleapis.com/css2?family=Signika:wght@600&family=Arimo:ital,wght@0,400;0,700;1,400&family=Tinos&display=swap">
<style>
  :root {
    --page: #ffffff;
    --card-dark: #0d0d0e;
    --card-mid: #2a2a2c;
    --card-light: #525255;
    --silver-metal: #c8c9cc;
    --silver-soft: #d0d0d2;
    --text-light: #e4e4e6;
    --text-muted: #a9a9ad;
    --rule: rgba(255,255,255,0.18);
  }
  * { margin: 0; padding: 0; box-sizing: border-box; }
  html, body {
    width: 1200px; height: 1200px; overflow: hidden;
    background: var(--page);
  }
  .canvas { position: relative; width: 1200px; height: 1200px; }

  .card {
    position: absolute;
    width: 942px; height: 537px;
    overflow: hidden;
  }
  .card--front { left: 101px; top: 30px; }
  .card--back  { left: 104px; top: 603px; }

  .card__backdrop {
    position: absolute; inset: 0;
    background:
      radial-gradient(ellipse 70% 90% at 95% 10%, var(--card-light) 0%, transparent 70%),
      radial-gradient(ellipse 60% 70% at 10% 85%, #050505 0%, transparent 75%),
      linear-gradient(115deg, var(--card-dark) 0%, var(--card-mid) 45%, var(--card-light) 100%);
  }

  .wordmark {
    position: absolute;
    font-family: "Signika", "Trebuchet MS", sans-serif;
    font-weight: 600;
    color: var(--silver-metal);
    letter-spacing: 1px;
    line-height: 1;
    white-space: nowrap;
  }
  .card--front .wordmark { left: 92px; top: 178px; font-size: 116px; }
  .card--back .wordmark  { left: 70px; top: 58px;  font-size: 94px; }

  .tagline {
    position: absolute;
    font-family: "Arimo", Arial, sans-serif;
    font-style: italic;
    color: var(--text-muted);
    white-space: nowrap;
  }
  .card--front .tagline {
    left: 0; right: 0; top: 404px;
    text-align: center; font-size: 22px; letter-spacing: 0.5px;
  }
  .card--back .tagline {
    right: 30px; bottom: 28px; font-size: 16px;
  }

  .front-url {
    position: absolute; left: 0; right: 0; top: 462px;
    text-align: center;
    font-family: "Tinos", "Times New Roman", serif;
    font-size: 20px;
    color: var(--text-light);
  }

  .contact-person {
    position: absolute; left: 714px; top: 250px;
    font-family: "Arimo", Arial, sans-serif;
    color: var(--silver-soft);
  }
  .contact-person__name { font-size: 26px; font-weight: 700; line-height: 1; }
  .contact-person__role { font-size: 18px; font-style: italic; margin-top: 4px; margin-left: 4px; color: var(--text-light); }

  .divider {
    position: absolute; left: 0; right: 0; top: 307px; height: 2px;
    background: linear-gradient(90deg, transparent 0%, var(--rule) 20%, var(--rule) 75%, transparent 100%);
  }

  .contact-list {
    position: absolute; left: 24px; top: 352px;
    list-style: none;
    font-family: "Arimo", Arial, sans-serif;
    font-size: 19px;
    color: var(--text-light);
  }
  .contact-list__item {
    display: flex; align-items: center;
    height: 28px; margin-bottom: 13px;
  }
  .contact-list__icon {
    width: 24px; height: 22px; margin-right: 26px; flex: none;
    fill: none; stroke: var(--text-light); stroke-width: 2;
  }
  .contact-list__badge {
    width: 24px; margin-right: 26px; flex: none;
    font-size: 13px; font-weight: 700; letter-spacing: 0.3px;
    text-align: center; color: var(--text-light);
  }
</style>
</head>
<body>
<main class="canvas">

  <section class="card card--front" aria-label="Card front">
    <div class="card__backdrop" role="img" aria-label="Dark flowing satin drapery background"></div>
    <h1 class="wordmark">KVTglassworks</h1>
    <p class="tagline">your local automotive &amp; machinery glass specialist</p>
    <p class="front-url">www.kvtglassworks.com.au</p>
  </section>

  <section class="card card--back" aria-label="Card back">
    <div class="card__backdrop" role="img" aria-label="Dark flowing satin drapery background"></div>
    <h2 class="wordmark">KVTglassworks</h2>

    <div class="contact-person">
      <p class="contact-person__name">Morris Hartley</p>
      <p class="contact-person__role">Managing Director</p>
    </div>

    <div class="divider"></div>

    <ul class="contact-list">
      <li class="contact-list__item">
        <svg class="contact-list__icon" viewBox="0 0 24 22" aria-hidden="true">
          <path d="M6 2 Q2 6 5 12 Q9 19 16 20 Q19 20 20 17 L16 14 L13 16 Q9 13 8 9 L10 6 Z" fill="var(--text-light)" stroke="none"/>
        </svg>
        <span>0482657193</span>
      </li>
      <li class="contact-list__item">
        <span class="contact-list__badge">ABN</span>
        <span>52840193657</span>
      </li>
      <li class="contact-list__item">
        <svg class="contact-list__icon" viewBox="0 0 24 22" aria-hidden="true">
          <rect x="3" y="5" width="18" height="13" fill="var(--text-light)" stroke="none"/>
          <path d="M3 5 L12 12 L21 5" stroke="#333" stroke-width="1.5"/>
        </svg>
        <span>morris@kvtglassworks.com.au</span>
      </li>
      <li class="contact-list__item">
        <svg class="contact-list__icon" viewBox="0 0 24 22" aria-hidden="true">
          <rect x="3" y="3" width="18" height="12" stroke-width="2"/>
          <path d="M12 15 V19 M7 19 H17" stroke-width="2"/>
        </svg>
        <span>www.kvtglassworks.com.au</span>
      </li>
    </ul>

    <p class="tagline">your local automotive &amp; machinery glass specialist</p>
  </section>

</main>
</body>
</html>
```